Harbor Crest Physician Advising

I need a one-page advertisement that I can email to potential clients.

The target audience is hospital administrators.

I want it to include the logo, as attached. We specialize in Payer Denial Management. We are certified physician advisors with over 80 years combined clinical medicine experience. We have expertise in Utilization Management, Clinical Documentation Integrity, Peer to Peer Appeals and Letter Appeal Management. We win over 60% of our Peer to Peer Appeals with Medicare Advantage plans and over 50% of our first level letters.

We make sure hospitals get paid for the care they provide, I really want to emphasize that we are very effective at overturning insurance payment denials. We also provider other physician advising services. We keep our company small so that our rates are very affordable. Include that references are available.

We need to include: Contact us today, we can improve your revenue. Please 304-555-0183
or email (I will provide this later).

I want it to look professional but not bland, with maybe AI created images of a small group of physicians (mature, white coats, stethoscopes) looking at a spreadsheet on a laptop. a picture of a stack of money setting on a table, with a hand removing part of the money from the stack.

Companies like ours include Quorvix, T7, Pellingham, Car-Nova, and TelvanMD. Their websites may provide ideas.

Target Market(s)

Healthcare administrators who need to improve their hospital revenue

Industry/Entity Type

Healthcare consulting

Font styles to use
Sans Serif

Colors
0094D4
00A9DD
6FCCEA
C7EBF8
E9F6FB
00AB8E
00BBA5
67D7C9
C6EFE9
E9F9F6
FFC000
F8CF3A
FAE287
FDF2CF
FEFAEE
EE7325
F08F49
F5BC92
FAE3D3
FDF4ED
E54698
E96AAD
F1A4CE
F9D9EA
FCEFF6
6B429C
8869AF
B7A5CE
E3DAEB
F3F0F8

Requirements
Must have
• Must include that we are very successful here to appear in Peer to Peer appeals and Letter appeals
Nice to have
• Very easy to read, big bold fonts
Should not have
• I’m very afraid of having a lot of dark blues, combined with dark gold, because it may look like the colors of a health system in my area

```html
<!DOCTYPE html>
<html lang="en">
<head>
<meta charset="utf-8">
<title>Harbor Crest Physician Advising – Denial Management</title>
<link rel="stylesheet" href="https://fonts.googleapis.com/css2?family=Open+Sans:wght@400;600;700;800&display=swap">
<style>
  :root{
    --navy:#0b3f7e;
    --navy-deep:#072c5c;
    --blue:#0094D4;
    --sky:#00A9DD;
    --sky-soft:#6FCCEA;
    --ice:#C7EBF8;
    --mist:#E9F6FB;
    --white:#ffffff;
    --ink:#0d3566;
  }
  *{box-sizing:border-box;margin:0;padding:0}
  html,body{width:1200px;height:2196px;overflow:hidden}
  body{font-family:"Open Sans",Arial,sans-serif;background:var(--mist);color:var(--ink)}
  .ad{position:relative;width:1200px;height:2196px;background:linear-gradient(180deg,#f4fbfe 0%,var(--mist) 45%,#dff1fa 100%);overflow:hidden}

  .hero-photo{position:absolute;left:0;top:0;width:1200px;height:640px;
    background:linear-gradient(160deg,#d9ecf6 0%,#b7d8ea 35%,#8fbcd6 60%,#e8f3f9 100%)}
  .brand-bar{position:absolute;left:0;top:0;width:1200px;height:110px;
    background:linear-gradient(90deg,var(--navy-deep) 0%,var(--navy) 40%,rgba(11,63,126,.55) 75%,rgba(11,63,126,0) 100%);
    display:flex;align-items:center;padding-left:28px;gap:18px}
  .brand-dot{width:62px;height:62px;border-radius:50%;background:var(--white)}
  .brand-name{color:var(--white);font-weight:700;font-size:40px;line-height:1;letter-spacing:1px}
  .brand-name small{display:block;font-size:20px;font-weight:600;letter-spacing:1.5px;margin-top:6px}

  .headline-band{position:absolute;left:0;top:632px;width:1200px;height:120px;
    background:linear-gradient(90deg,var(--navy-deep),var(--navy) 50%,var(--navy-deep));
    color:var(--white);text-align:center;font-size:38px;line-height:1.35;font-weight:600;
    display:flex;flex-direction:column;justify-content:center}

  .intro-card{position:absolute;left:100px;top:790px;width:1000px;height:250px;
    background:var(--white);border-radius:18px;border:2px solid var(--ice);
    box-shadow:0 8px 24px rgba(0,148,212,.15);text-align:center;padding-top:26px}
  .intro-card h2{font-size:38px;font-weight:600;color:var(--navy);margin-bottom:10px}
  .intro-card p{font-size:31px;line-height:1.32;color:var(--ink)}

  .panels-photo{position:absolute;left:0;top:1056px;width:1200px;height:590px;
    background:radial-gradient(ellipse at 30% 80%,#cfe3c8 0%,rgba(207,227,200,0) 45%),
               linear-gradient(180deg,#cfe7f4 0%,#a8d2ea 55%,#d9eef8 100%)}
  .panel{position:absolute;top:1070px;height:540px;border-radius:16px;
    background:linear-gradient(160deg,rgba(0,148,212,.78),rgba(11,63,126,.82));
    border:2px solid rgba(255,255,255,.55);color:var(--white);padding:34px 26px}
  .panel--services{left:48px;width:520px}
  .panel--results{left:584px;width:568px}
  .panel h3{text-align:center;font-size:34px;font-weight:700;letter-spacing:1px;margin-bottom:34px}
  .panel ul{list-style:none}
  .panel li{display:flex;gap:12px;align-items:flex-start;font-size:22px;line-height:1.3;margin-bottom:28px}
  .panel li svg{flex:0 0 22px;margin-top:3px}
  .chart{position:absolute;right:34px;bottom:30px}

  .callout{position:absolute;left:70px;top:1676px;width:1060px;height:150px;border-radius:14px;
    background:linear-gradient(90deg,var(--navy),var(--blue));color:var(--white);
    display:flex;align-items:center;justify-content:center;padding-left:90px;padding-right:20px;
    font-size:28px;line-height:1.4;font-weight:600;text-align:center;white-space:nowrap}
  .callout-icon{position:absolute;left:36px;top:26px;width:56px;height:56px;border-radius:50%;
    background:var(--white);color:var(--navy);font-weight:800;font-size:32px;display:flex;align-items:center;justify-content:center}

  .cta{position:absolute;left:330px;top:1848px;width:540px;height:90px;display:flex;align-items:center}
  .cta-phone{width:70px;height:90px}
  .cta-button{flex:1;height:84px;border-radius:14px;background:linear-gradient(180deg,var(--sky),var(--blue));
    color:var(--white);font-size:40px;font-weight:600;display:flex;align-items:center;justify-content:center;
    box-shadow:0 6px 16px rgba(0,148,212,.35)}
  .cta-note{position:absolute;left:0;top:1956px;width:1200px;text-align:center;font-size:24px;color:var(--navy)}

  .contact-bar{position:absolute;left:0;top:2000px;width:1200px;height:70px;background:var(--navy);
    color:var(--white);display:flex;align-items:center;justify-content:space-between;padding:0 40px}
  .contact-item{display:flex;align-items:center;gap:16px;font-size:28px}
  .contact-item--phone{font-size:44px;font-weight:600}

  .footer{position:absolute;left:0;top:2070px;width:1200px;height:126px;background:var(--ice);
    text-align:center;color:var(--navy);font-size:24px;line-height:1.35;padding-top:12px}
</style>
</head>
<body>
<main class="ad">
  <div class="hero-photo" role="img" aria-label="Photo of a small group of mature physicians in white coats reviewing a spreadsheet on a laptop"></div>
  <header class="brand-bar">
    <span class="brand-dot"></span>
    <div class="brand-name">HARBOR CREST<small>PHYSICIAN ADVISING</small></div>
  </header>

  <section class="headline-band">
    <div>Is Your Hospital Losing Money Due to Payment Denials?</div>
    <div>We help you recover it.</div>
  </section>

  <section class="intro-card">
    <h2>Denial Management Advisors</h2>
    <p>Certified physician advisors with over 80 years of combined<br>clinical experience, specializing in overturning payment denials<br>from insurers, including Medicare Advantage plans.</p>
  </section>

  <div class="panels-photo" role="img" aria-label="Photo of a stack of money on a table with a hand removing part of it"></div>

  <section class="panel panel--services">
    <h3>OUR SERVICES</h3>
    <ul>
      <li><svg width="22" height="22" viewBox="0 0 24 24"><path d="M4 12l5 5L20 6" fill="none" stroke="#fff" stroke-width="3"/></svg>Peer-to-peer (P2P) appeals</li>
      <li><svg width="22" height="22" viewBox="0 0 24 24"><path d="M4 12l5 5L20 6" fill="none" stroke="#fff" stroke-width="3"/></svg>First level appeal letters</li>
      <li><svg width="22" height="22" viewBox="0 0 24 24"><path d="M4 12l5 5L20 6" fill="none" stroke="#fff" stroke-width="3"/></svg>Utilization management (UM)</li>
      <li><svg width="22" height="22" viewBox="0 0 24 24"><path d="M4 12l5 5L20 6" fill="none" stroke="#fff" stroke-width="3"/></svg>Clinical documentation integrity (CDI)</li>
      <li><svg width="22" height="22" viewBox="0 0 24 24"><path d="M4 12l5 5L20 6" fill="none" stroke="#fff" stroke-width="3"/></svg>Strategic medical advisory and consulting</li>
    </ul>
  </section>

  <section class="panel panel--results">
    <h3>PROVEN RESULTS</h3>
    <ul>
      <li><svg width="22" height="22" viewBox="0 0 24 24"><path d="M4 12l5 5L20 6" fill="none" stroke="#fff" stroke-width="3"/></svg>Over 60% success rate in peer-to-peer appeals</li>
      <li><svg width="22" height="22" viewBox="0 0 24 24"><path d="M4 12l5 5L20 6" fill="none" stroke="#fff" stroke-width="3"/></svg>Over 50% success rate in first-level written appeals</li>
      <li><svg width="22" height="22" viewBox="0 0 24 24"><path d="M4 12l5 5L20 6" fill="none" stroke="#fff" stroke-width="3"/></svg>Affordable rates – we are a boutique firm, focused on value</li>
      <li><svg width="22" height="22" viewBox="0 0 24 24"><path d="M4 12l5 5L20 6" fill="none" stroke="#fff" stroke-width="3"/></svg>References available upon request</li>
    </ul>
    <svg class="chart" width="110" height="100" viewBox="0 0 110 100">
      <rect x="6" y="66" width="16" height="30" fill="#6FCCEA"/>
      <rect x="32" y="50" width="16" height="46" fill="#6FCCEA"/>
      <rect x="58" y="34" width="16" height="62" fill="#C7EBF8"/>
      <rect x="84" y="16" width="16" height="80" fill="#fff"/>
      <path d="M6 56 L40 36 L62 44 L100 6" fill="none" stroke="#fff" stroke-width="4"/>
      <path d="M88 6 L102 4 L100 18" fill="none" stroke="#fff" stroke-width="4"/>
    </svg>
  </section>

  <section class="callout">
    <span class="callout-icon">$</span>
    <div>Make sure your hospital gets paid for the care it provides.<br>Our physician advisors work with you — not with the insurers.</div>
  </section>

  <div class="cta">
    <svg class="cta-phone" viewBox="0 0 70 90"><path d="M18 22c4-4 8-4 10 0l6 10c2 3 1 6-2 8l-4 3c3 8 9 15 17 19l3-4c2-3 5-4 8-2l9 6c4 2 4 6 0 10l-5 5c-4 4-12 4-20-2C26 66 14 52 10 38 8 30 10 26 14 24z" fill="#0b3f7e"/><path d="M44 18a22 22 0 0 1 18 18M42 6a34 34 0 0 1 26 28" fill="none" stroke="#00A9DD" stroke-width="4"/></svg>
    <div class="cta-button">Contact us today</div>
  </div>
  <p class="cta-note">we can help increase your revenue.</p>

  <section class="contact-bar">
    <div class="contact-item">
      <svg width="40" height="28" viewBox="0 0 40 28"><rect x="2" y="2" width="36" height="24" fill="none" stroke="#fff" stroke-width="3"/><path d="M2 2l18 14L38 2" fill="none" stroke="#fff" stroke-width="3"/></svg>
      [your-email@domain.com]
    </div>
    <div class="contact-item contact-item--phone">
      <svg width="30" height="46" viewBox="0 0 30 46"><rect x="2" y="2" width="26" height="42" rx="5" fill="none" stroke="#fff" stroke-width="3"/><circle cx="15" cy="37" r="3" fill="#fff"/></svg>
      304-555-0183
    </div>
  </section>

  <footer class="footer">
    Trusted strategies like ours are used by:<br>
    Quorvix | T7 | Pellingham | Car-Nova | TelvanMD<br>
    But we offer more attention, more flexibility, and better value.
  </footer>
</main>
</body>
</html>
```